Business cards design on a high standard

We advise clients on insurance and financial matters, since these clients pay for our advice, the design should have a high standard. Our logo should be included. From the colors we are open for everything.

Colors

Designer to choose colors to be used in the design.

```html
<!DOCTYPE html>
<html lang="en">
<head>
<meta charset="utf-8">
<title>Alpine Counsel – Business Cards</title>
<link href="https://fonts.googleapis.com/css2?family=Lato:wght@400;700&display=swap" rel="stylesheet">
<style>
  :root {
    --backdrop: #dedede;
    --brand-red: #d61f26;
    --swoosh-grey: #a3a3a3;
    --text-grey: #8c8c8c;
    --divider-grey: #b5b5b5;
    --paper: #ffffff;
  }
  * { margin: 0; padding: 0; box-sizing: border-box; }
  html, body {
    width: 1200px;
    height: 960px;
    overflow: hidden;
    background: var(--backdrop);
    font-family: "Lato", sans-serif;
  }
  .card {
    position: absolute;
    left: 280px;
    width: 656px;
    height: 375px;
    border-radius: 24px;
    overflow: hidden;
    box-shadow: 0 3px 4px rgba(0, 0, 0, 0.35);
  }
  .card--front { top: 80px; }
  .card--back { top: 506px; background: var(--brand-red); }
  .card__art { position: absolute; inset: 0; }

  .wordmark {
    position: absolute;
    text-align: center;
    font-weight: 700;
    line-height: 1;
  }
  .wordmark__main { display: block; letter-spacing: 1px; }
  .wordmark__sub { display: block; letter-spacing: 6px; }

  .card--front .wordmark {
    left: 82px;
    top: 166px;
    width: 220px;
    color: var(--brand-red);
  }
  .card--front .wordmark__main { font-size: 38px; }
  .card--front .wordmark__sub { font-size: 17px; margin-top: 4px; }

  .divider {
    position: absolute;
    left: 326px;
    top: 114px;
    width: 2px;
    height: 140px;
    background: var(--divider-grey);
  }
  .contact-block {
    position: absolute;
    left: 356px;
    top: 110px;
  }
  .contact-block__name {
    font-size: 27px;
    font-weight: 700;
    color: var(--brand-red);
  }
  .contact-block__role {
    font-size: 18px;
    color: var(--text-grey);
    margin-top: 2px;
  }
  .contact-list {
    list-style: none;
    margin-top: 20px;
  }
  .contact-list li {
    display: flex;
    align-items: center;
    gap: 8px;
    font-size: 17.5px;
    color: var(--text-grey);
    height: 24px;
  }
  .contact-list svg { width: 14px; height: 14px; flex: none; }

  .card--back .wordmark {
    left: 0;
    width: 656px;
    top: 150px;
    color: var(--paper);
  }
  .card--back .wordmark__main { font-size: 56px; }
  .card--back .wordmark__sub { font-size: 25px; letter-spacing: 8px; margin-top: 6px; }
  .card__url {
    position: absolute;
    left: 0;
    width: 656px;
    top: 316px;
    text-align: center;
    font-size: 16.5px;
    color: var(--paper);
  }
</style>
</head>
<body>

<section class="card card--front" aria-label="Card front">
  <svg class="card__art" viewBox="0 0 656 375" aria-hidden="true">
    <rect width="656" height="375" fill="var(--brand-red)"/>
    <path d="M0 150 C 20 60, 110 8, 262 0 L 656 0 L 656 230 C 640 330, 560 372, 440 375 L 0 375 Z" fill="var(--swoosh-grey)"/>
    <path d="M0 120 C 30 45, 120 2, 242 0 L 656 0 L 656 206 C 630 320, 540 372, 422 375 L 0 375 Z" fill="var(--paper)"/>
  </svg>

  <div class="wordmark">
    <span class="wordmark__main">ALPINE</span>
    <span class="wordmark__sub">COUNSEL</span>
  </div>

  <div class="divider"></div>

  <div class="contact-block">
    <p class="contact-block__name">Mara Lindqvist</p>
    <p class="contact-block__role">CEO &amp; Founder</p>
    <ul class="contact-list">
      <li>
        <svg viewBox="0 0 14 14" aria-hidden="true"><path d="M3 1 L5.5 3.5 L4 5.5 C5 7.5 6.5 9 8.5 10 L10.5 8.5 L13 11 L11 13 C6 13 1 8 1 3 Z" fill="var(--brand-red)"/></svg>
        (555) 010 2040
      </li>
      <li>
        <svg viewBox="0 0 14 14" aria-hidden="true"><rect x="1" y="3" width="12" height="8" fill="var(--brand-red)"/><path d="M1 3 L7 8 L13 3" stroke="#fff" stroke-width="1.2" fill="none"/></svg>
        hello@alpinecounsel.com
      </li>
      <li>
        <svg viewBox="0 0 14 14" aria-hidden="true"><circle cx="7" cy="7" r="5.5" fill="none" stroke="var(--brand-red)" stroke-width="1.4"/><ellipse cx="7" cy="7" rx="2.4" ry="5.5" fill="none" stroke="var(--brand-red)" stroke-width="1.2"/><path d="M1.5 7 H12.5" stroke="var(--brand-red)" stroke-width="1.2"/></svg>
        www.alpinecounsel.com
      </li>
    </ul>
  </div>
</section>

<section class="card card--back" aria-label="Card back">
  <div class="wordmark">
    <span class="wordmark__main">ALPINE</span>
    <span class="wordmark__sub">COUNSEL</span>
  </div>
  <p class="card__url">www.alpinecounsel.com</p>
</section>

</body>
</html>
```